Page Layouts for Australian Political Party

The Horizon Civic Movement of Australia has a design for its logo and now is looking for a website proposal. The initial website is being powered by blogger with plans to move to an ExpressionEngine based site. The current website is at www.hcmvote.org

Its likely if we see a design within the next 2 days we like it will be selected before the 5 days has expired.

Target Market(s)

Looking for a design that will appeal to both the "online" generation as well as more casual internet users. These users might be comfortable with online banking and perhaps hotmail/skype but not much more.

I personally like the "feel" of plivor.com and wembalytics.com. You might like to look at the other major political parties in Australia to see what probably quite a lot of "market testing" and money is acceptable to the Australian population. We are aiming for Generation X and younger and well as the baby boomers who get the 2.0 internet.

Industry/Entity Type

Political

Requirements
Must have
• The ability to scale elegantly across a full ExpressionEngine implementation, forums, blogs, homepage etc.
• Also look elegant on the initial blogger driven page.
• Navigation that could contain all the items on the www.tandrum.org.au site, you can use these as the place holder names for the navigation design. The short name for the party is HCM. The
Nice to have
• feel distinct from the other major parties websites. we do have views more in line with the rovers/pathmakers in this country.
Should not have
• basic stuff, not look like a kloobnet page ;) imagery too similar from any of the other parties...

```html
<!DOCTYPE html>
<html lang="en">
<head>
<meta charset="utf-8">
<title>Horizon Civic Movement of Australia</title>
<link rel="stylesheet" href="https://fonts.googleapis.com/css2?family=PT+Sans:wght@400;700&family=Tinos:ital@0;1&family=Arimo&display=swap">
<style>
  :root {
    --bar-dark: #0f4d66;
    --bar-mid: #1f6f8f;
    --bar-light: #2c84a6;
    --page-top: #f4f5f6;
    --page-bottom: #e3e7ea;
    --ink: #2b2b2b;
    --ink-soft: #555555;
    --date: #6d6d6d;
    --heading-red: #7a2c1e;
    --rule-orange: #d9783c;
    --party-box: #ece2d6;
    --ideas-box: rgba(214, 220, 206, 0.85);
    --item-red: #b4533b;
    --item-green: #5c7b3c;
    --item-blue: #243a76;
    --rule-blue: #2a3f6e;
    --footer-text: #e8f4f8;
    --logo-blue: #1d5a8c;
    --frame: #d6d6d6;
  }
  * { box-sizing: border-box; margin: 0; padding: 0; }
  html, body { width: 1166px; height: 1200px; overflow: hidden; }
  body {
    position: relative;
    background: linear-gradient(180deg, var(--page-top) 0%, var(--page-bottom) 100%);
    font-family: "Tinos", "Times New Roman", serif;
    color: var(--ink);
  }

  .top-nav {
    position: absolute; left: 0; top: 0; width: 1166px; height: 65px;
    background: linear-gradient(180deg, var(--bar-light) 0%, var(--bar-mid) 45%, var(--bar-dark) 100%);
    border-top: 2px solid #7a3a20;
    box-shadow: 0 3px 6px rgba(0,0,0,0.25);
    display: flex; justify-content: center; align-items: center;
  }
  .top-nav a {
    font-family: "PT Sans", Tahoma, sans-serif; font-size: 19px; color: #fff;
    text-decoration: none; padding: 0 7px; line-height: 28px;
    border-left: 1px solid rgba(255,255,255,0.75);
  }
  .top-nav a:first-child { border-left: none; }

  .search {
    position: absolute; left: 871px; top: 93px;
    display: flex; align-items: center;
    font-family: "Arimo", Arial, sans-serif; font-size: 14px; color: var(--ink-soft);
  }
  .search input {
    margin-left: 12px; width: 173px; height: 25px;
    border: 1px solid #8ea4c0; border-radius: 5px; background: #fff;
  }
  .search svg { margin-left: 12px; }

  .brand {
    position: absolute; left: 41px; top: 96px;
    display: flex; flex-direction: column; align-items: center; width: 150px;
  }
  .brand-mark { width: 56px; height: 56px; background: var(--logo-blue); border-radius: 6px; }
  .brand-name {
    margin-top: 8px; font-family: "PT Sans", Tahoma, sans-serif; font-size: 19px;
    color: var(--ink); white-space: nowrap;
  }

  .quick-links {
    position: absolute; left: 356px; top: 148px; display: flex; gap: 28px;
  }
  .quick-links a {
    font-family: "PT Sans", Tahoma, sans-serif; font-size: 25px; color: #111;
    text-decoration: underline; text-underline-offset: 3px;
  }

  .hero-frame {
    position: absolute; left: 40px; top: 192px; width: 687px; height: 305px;
    border: 1px solid var(--frame); border-radius: 8px; background: #f7f7f7;
    box-shadow: 0 1px 3px rgba(0,0,0,0.12);
  }
  .hero-photo {
    position: absolute; left: 8px; top: 8px; width: 669px; height: 288px;
    background: radial-gradient(ellipse at 30% 50%, #6b5a4a 0%, #8b6e55 35%, #c48a62 70%, #b47a56 100%);
  }

  .party-intro {
    position: absolute; left: 750px; top: 194px; width: 385px; min-height: 303px;
    background: var(--party-box); padding: 6px 14px 8px 19px;
  }
  .party-intro h1 {
    font-family: "PT Sans", Tahoma, sans-serif; font-size: 25px; font-weight: 700;
    color: var(--ink-soft); margin-bottom: 8px;
  }
  .party-intro p { font-size: 14.8px; line-height: 20.6px; }

  .feature-list { position: absolute; left: 41px; top: 555px; width: 214px; }
  .feature {
    font-size: 15.4px; line-height: 19.4px; padding-bottom: 18px; margin-bottom: 18px;
  }
  .feature:last-child { padding-bottom: 0; margin-bottom: 0; }
  .feature-thumb {
    float: left; width: 53px; height: 49px; margin: 0 8px 2px 0;
    border: 1px solid #8a8a8a; border-radius: 3px;
    background: linear-gradient(135deg, #eae2d6 0%, #c99b72 50%, #7b5a44 100%);
  }
  .feature.red { color: var(--item-red); border-bottom: 1px solid var(--rule-orange); }
  .feature.green { color: var(--item-green); border-bottom: 1px solid var(--rule-blue); }
  .feature.blue { color: var(--item-blue); }

  .section-title {
    font-family: "PT Sans", Tahoma, sans-serif; font-size: 28px; font-weight: 400;
    color: var(--heading-red); border-bottom: 2px solid var(--rule-orange);
    padding-bottom: 2px;
  }

  .latest-news { position: absolute; left: 319px; top: 542px; width: 470px; }
  .latest-news .section-title { width: 453px; margin-bottom: 14px; }
  .news-item { margin-bottom: 22px; }
  .news-date { font-style: italic; font-size: 14.8px; color: var(--date); line-height: 21.7px; }
  .news-item p { font-size: 14.8px; line-height: 21.7px; }

  .your-ideas { position: absolute; left: 829px; top: 542px; width: 291px; }
  .your-ideas .section-title { margin-bottom: 10px; }
  .ideas-box {
    margin-left: 3px; background: var(--ideas-box);
    padding: 4px 12px 8px 18px;
  }
  .ideas-box p { font-size: 14.8px; line-height: 21.7px; }

  .site-footer {
    position: absolute; left: 0; top: 985px; width: 1166px; height: 215px;
    background: radial-gradient(ellipse at 50% 40%, #2b7a9a 0%, #1d6485 55%, #0e435a 100%);
    box-shadow: 0 -6px 10px rgba(0,0,0,0.22);
  }
  .footer-col { position: absolute; top: 30px; list-style: none; }
  .footer-col li {
    font-family: "Arimo", Arial, sans-serif; font-size: 13.7px; line-height: 27.4px;
    color: var(--footer-text);
  }
</style>
</head>
<body>

<nav class="top-nav">
  <a href="#">Economy</a><a href="#">Small Business</a><a href="#">National Security</a><a href="#">Community</a><a href="#">Seniors</a><a href="#">Health</a><a href="#">Education</a><a href="#">Environment</a><a href="#">Regional</a><a href="#">Infrastructure</a>
</nav>

<form class="search">
  <label for="q">Search:</label>
  <input id="q" type="text">
  <svg width="26" height="26" viewBox="0 0 26 26" aria-hidden="true">
    <circle cx="15" cy="10" r="7.5" fill="#f2f2f2" stroke="#9a9a9a" stroke-width="2"/>
    <line x1="9.5" y1="15.5" x2="3" y2="22" stroke="#8a8a8a" stroke-width="3.5" stroke-linecap="round"/>
  </svg>
</form>

<div class="brand">
  <div class="brand-mark"></div>
  <div class="brand-name">Horizon Civic</div>
</div>

<div class="quick-links">
  <a href="#">Donate</a><a href="#">Get Involved</a><a href="#">Contact Us</a>
</div>

<div class="hero-frame">
  <div class="hero-photo" role="img" aria-label="Close-up photograph of a kangaroo's head against a soft warm background"></div>
</div>

<section class="party-intro">
  <h1>Horizon Civic Movement</h1>
  <p>Lorem ipsum dolor sit amet, consectetur adipiscing elit. Sed at convallis ante. Pellentesque dolor enim, hendrerit vitae malesuada eget, consectetur vitae sem. Cras lacus quam, dignissim id pretium nec, pretium semper turpis. Donec faucibus pulvinar leo id rutrum. Aenean tincidunt placerat mi eget aliquet. In placerat porttitor condimentum. Curabitur mattis, dolor pulvinar tempus adipiscing, sapien orci porta metus, eu condimentum erat erat at purus. Pellentesque habitant morbi tristique senectus et netus et malesuada fames ac turpis egestas. Integer tempor pharetra tortor a cursus. Proin hendrerit ultrices tellus, in sollicitudin purus</p>
</section>

<aside class="feature-list">
  <div class="feature red">
    <div class="feature-thumb" role="img" aria-label="Small photograph of a handshake"></div>
    Lorem ipsum dolor sit consectetur adipiscing Sed at convallis ante. Pellen tesque dolor enim, hendrerit vitae malesuada eget,
  </div>
  <div class="feature green">
    <div class="feature-thumb" role="img" aria-label="Small photograph of a handshake"></div>
    Lorem ipsum dolor sit consectetur adipiscing Sed at convallis ante. Pellen tesque dolor enim, hendrerit vitae malesuada eget,
  </div>
  <div class="feature blue">
    <div class="feature-thumb" role="img" aria-label="Small photograph of a handshake"></div>
    Lorem ipsum dolor sit consectetur adipiscing Sed at convallis ante. Pellen tesque dolor enim, hendrerit vitae malesuada eget,
  </div>
</aside>

<section class="latest-news">
  <h2 class="section-title">Latest News</h2>
  <article class="news-item">
    <div class="news-date">11/02/10</div>
    <p>Lorem ipsum dolor sit amet, consectetur adipiscing elit. Sed at convallis ante. Pellentesque dolor enim, hendrerit vitae malesuada eget, consectetur vitae sem.Cras lacus quam, dignissim id pretium nec, pretium semper turpis.</p>
  </article>
  <article class="news-item">
    <div class="news-date">11/02/10</div>
    <p>Donec faucibus pulvinar leo id rutrum. Aenean tincidunt placerat mi eget aliquet. In placerat porttitor condimentum. Curabitur mattis, dolor pulvinar tempus adipiscing, sapien orci porta metus, eu condimentum erat erat at purus.</p>
  </article>
  <article class="news-item">
    <div class="news-date">11/02/10</div>
    <p>Pellentesque habitant morbi tristique senectus et netus et malesuada fames ac turpis egestas. Integer tempor pharetra tortor a cursus. Proin hendrerit ultrices</p>
  </article>
</section>

<section class="your-ideas">
  <h2 class="section-title">Your Ideas</h2>
  <div class="ideas-box">
    <p>Lorem ipsum dolor sit amet, consectetur adipiscing elit. Sed at convallis ante. Pellentesque dolor enim, hendrerit vitae malesuada eget, consectetur vitae sem. Cras lacus quam, dignissim id pretium nec, pretium semper turpis. Donec faucibus pulvinar leo id rutrum. Aenean tincidunt placerat mi eget aliquet. In placerat porttitor condimentum. Curabitur mattis, dolor pulvinar tempus adipiscing, sapien orci porta metus, eu condimentum erat erat at purus. Pellentesque habitant morbi tristique senectus et netus et malesuada fames ac turpis egestas. Integer tempor pharetra tortor a cursus. Proin hendrerit</p>
  </div>
</section>

<footer class="site-footer">
  <ul class="footer-col" style="left:88px">
    <li>Lorem ipsum</li><li>Dolor sit ametcon</li><li>Sectetur adipisci</li><li>Sed at convallis ante.</li><li>Pellentesque dolor</li>
  </ul>
  <ul class="footer-col" style="left:362px">
    <li>Lorem ipsum</li><li>Dolor sit ametcon</li><li>Sectetur adipisci</li><li>Sed at convallis ante.</li><li>Pellentesque dolor</li>
  </ul>
  <ul class="footer-col" style="left:657px">
    <li>Lorem ipsum</li><li>Dolor sit ametcon</li><li>Sectetur adipisci</li><li>Sed at convallis ante.</li><li>Pellentesque dolor</li>
  </ul>
  <ul class="footer-col" style="left:958px">
    <li>Lorem ipsum</li><li>Dolor sit ametcon</li><li>Sectetur adipisci</li><li>Sed at convallis ante.</li><li>Pellentesque dolor</li>
  </ul>
</footer>

</body>
</html>
```